New Turmel Business Card Design

We need a business card to match our new branding. The look should utilize the elements as attached here (Vector files & new exec overview are attached.) I really like 'organic' looking elements (e.g. an idea would be to have this printed on recycled paper stock). Thank you! Looking forward to seeing your designs.

Business

```html
<!DOCTYPE html>
<html lang="en">
<head>
<meta charset="utf-8">
<title>Turmel Business Card</title>
<link rel="stylesheet" href="https://fonts.googleapis.com/css2?family=Didact+Gothic&family=Questrial&display=swap">
<style>
  :root {
    --page-bg: #ecebe8;
    --card-white: #ffffff;
    --brand-blue: #2176bd;
    --brand-blue-light: #5d9fd6;
    --brand-green: #8cc63f;
    --text-grey: #8a8a8a;
    --rule-grey: #c9c9c9;
    --shadow: rgba(0,0,0,0.18);
  }
  * { margin: 0; padding: 0; box-sizing: border-box; }
  html, body { width: 1200px; height: 841px; overflow: hidden; }
  body {
    background: var(--page-bg);
    font-family: "Didact Gothic", "Century Gothic", sans-serif;
    position: relative;
  }
  .card {
    position: absolute;
    top: 270px;
    width: 525px;
    height: 300px;
    overflow: hidden;
    box-shadow: 0 6px 18px var(--shadow);
  }
  .card--front { left: 50px; background: var(--card-white); }
  .card--back  { left: 625px; background: var(--brand-blue); }

  /* Front */
  .brand {
    position: absolute;
    display: flex;
    align-items: center;
    gap: 12px;
  }
  .brand__dot {
    width: 40px; height: 40px; border-radius: 50%;
    background: var(--brand-green);
  }
  .brand__name {
    font-family: "Questrial", sans-serif;
    font-size: 54px;
    line-height: 1;
    letter-spacing: -1px;
  }
  .card--front .brand { left: 30px; top: 108px; }
  .card--front .brand__name { color: var(--brand-blue); }

  .contact {
    position: absolute;
    left: 300px; top: 28px;
    padding-left: 14px;
    border-left: 1px solid var(--rule-grey);
    height: 190px;
    color: var(--text-grey);
    font-size: 15px;
    line-height: 1.2;
  }
  .contact__name { color: var(--brand-green); font-size: 18px; }
  .contact__title { font-size: 17px; margin-bottom: 10px; }
  .contact__address { margin-bottom: 8px; }
  .contact__row { display: flex; align-items: center; gap: 7px; height: 19px; }
  .contact__icon { width: 13px; height: 13px; fill: var(--brand-green); flex: none; }

  .bands { position: absolute; left: 0; bottom: 0; width: 525px; height: 90px; }

  /* Back */
  .card--back .brand { left: 170px; top: 100px; }
  .card--back .brand__name { color: var(--card-white); font-size: 62px; }
  .partner-badge {
    position: absolute; left: 26px; top: 36px;
    width: 52px; height: 30px;
    background: var(--card-white);
    opacity: 0.85;
  }
  .practice {
    position: absolute; right: 24px; bottom: 26px;
    text-align: right;
    color: var(--card-white);
  }
  .practice__name { font-size: 15px; letter-spacing: 0.5px; }
  .practice__rule { height: 1px; background: var(--card-white); opacity: 0.7; margin: 3px 0; }
  .practice__label { font-size: 8px; letter-spacing: 1.5px; }
</style>
</head>
<body>

<section class="card card--front" aria-label="Card front">
  <div class="brand">
    <span class="brand__dot"></span>
    <span class="brand__name">Turmel</span>
  </div>

  <div class="contact">
    <p class="contact__name">Your Name</p>
    <p class="contact__title">President</p>
    <p class="contact__address">Sample Lane 420<br>Bayvale 0000 North</p>
    <p class="contact__row">
      <svg class="contact__icon" viewBox="0 0 16 16"><rect x="4" y="0" width="8" height="16" rx="1.5"/></svg>111-111-1111
    </p>
    <p class="contact__row">
      <svg class="contact__icon" viewBox="0 0 16 16"><path d="M3 1l3 0 1.5 4-2 1.5c1 2 2.5 3.5 4.5 4.5l1.5-2 4 1.5v3c0 1-1 1.5-2 1.5C6 15 1 10 1 3c0-1 1-2 2-2z"/></svg>111-111-1111
    </p>
    <p class="contact__row">
      <svg class="contact__icon" viewBox="0 0 16 16"><rect x="4" y="1" width="8" height="5"/><rect x="1" y="6" width="14" height="9" rx="1"/></svg>111-111-1111
    </p>
    <p class="contact__row">
      <svg class="contact__icon" viewBox="0 0 16 16"><path d="M1 3h14v10H1z M1 3l7 6 7-6" stroke="#fff" stroke-width="1"/></svg>hello@turmel.au
    </p>
    <p class="contact__row">
      <svg class="contact__icon" viewBox="0 0 16 16"><circle cx="8" cy="8" r="7"/><path d="M1 8h14M8 1c-3 4-3 10 0 14M8 1c3 4 3 10 0 14" stroke="#fff" fill="none"/></svg>www.turmel.com
    </p>
  </div>

  <svg class="bands" viewBox="0 0 525 90" preserveAspectRatio="none" aria-hidden="true">
    <polygon points="0,0 210,14 190,90 0,90" fill="var(--brand-blue)"/>
    <polygon points="210,14 290,24 270,90 190,90" fill="var(--brand-blue-light)"/>
    <polygon points="290,24 525,58 525,90 270,90" fill="var(--brand-green)" opacity="0.45"/>
    <polygon points="340,56 525,70 525,90 320,90" fill="var(--brand-green)"/>
  </svg>
</section>

<section class="card card--back" aria-label="Card back">
  <span class="partner-badge" aria-hidden="true"></span>
  <div class="brand">
    <span class="brand__dot"></span>
    <span class="brand__name">Turmel</span>
  </div>
  <div class="practice">
    <p class="practice__name">Northwind</p>
    <div class="practice__rule"></div>
    <p class="practice__label">CONSULTING PARTNER</p>
  </div>
</section>

</body>
</html>
```